Business Card and Letterhead for Juniper Anvil - (Have Logo)

Update 4: Removed company reg no from business card details as it looked a bit out of place. Updated services list.
UPDATE 3
Sorry, I got the address a little bit wrong, have updated it below. Sorry for any inconvenience caused.
UPDATE 2
Finally I have the details for the business cards and letterhead. Submissions already made do not have to be updated unless shortlisted, if all new submissions could include the details for me, Marcus, that would be very much appreciated and help with the final shortlist selection. I intend to share a shortlist of the three best entries with past and existing customers for their feedback and opinions. Thank you all again for your time.
Here are the details.
Marcus Telby
Web Developer
T: 01632 960 418
E: marcus@juniperanvil.example
www.juniperanvil.example
Professional Photography
Web Solutions & E-Commerce
Audio & HD Video Production
Marketing & Promotions
Identity and Branding
Juniper Anvil Ltd
Suite 20938, 3rd Floor
212-224 Orchard Lane
London, N7 9QX
Company Reg. No: 05829147
The order and the layout of the information are of course down to the design, but the company registration number should be smaller and less prominent. The formatting of the telephone and email address using a T: and an E: I am not sure about and again if it is Tel: or Email: or Icons is up to the design.
The Company No. on the letterhead should read (somewhere in small text along the bottom):
Juniper Anvil is a Ltd Company registered in England & Wales, Registration No. 05829147.
The second business card details are
Oliver Brackley
Photographer
T: 01632 960 418
E: oliver@juniperanvil.example
Everything else the same of course.
Thank you again for all the submissions so far.
END OF UPDATE 2
-
UPDATE 1: Please do not alter the logo nor the logo colours. (This was a previous pixel forum project and I am extremely happy with it. The icon can stand alone of course, but I have had to eliminate all entries that have made it black and white, or reversed the icon.) I would like to thank everyone that has participated so far and am very grateful for all your thought and time.
End of Update 1
-
Original Brief:
I have attached the logo vector file.
Following a superb logo from a previous Pixel Forum project I am now looking for a business card design and (although less important) a letterhead as well.
I must admit I tried to do it myself but could only come up with the usual amateur stuff that in comparison to the quality of the logo looked awful.
About Us
Juniper Anvil Ltd will be a new company due to start in January. It is really just me (a web developer) and my friend (a photographer). We will be aiming at the usual small to medium sized businesses in the local area, selling various digital services including photographic services to the public, web hosting and development, commercial photography, modelling services (not us!), full video and film production and possibly a bit of marketing as well. (Really it is anything we can do professionally all lumped together! We met running seperate businesses which have both since closed)
We will not be competing on price. We plan to be expensive but fair. Certainly not the cheapest.
What we are looking for
Business Card
I imagine a double sided business card, which will be used for more than one person. I imagine the front to be the same for everyone and the persons details to be on the back, although this is of course only my thoughts and I am of course completely open to any ideas.
The card could also have a services list or a bit about what we do on it. It might feature the website address, our business address (mail forwarding address) or our registered company number.
Or it might have none of that, we are completely open to any ideas and have no real fixed opinions. I just want it to be really nice :-)
Letterhead (secondary importance)
We will make our decision primarily on the business card, although a mathcing letterhead would be fantastic. Something standardish in format and simple, although again, all ideas are welcomed.
I hope that is enough information but if you have any questions I will answer them as fully and as quickly as possible.
Thank you once again and I really look forward to seeing your ideas and picking a winner.
Marcus T.
Small businesses AND the general public
Film Production

```html
<!DOCTYPE html>
<html lang="en">
<head>
<meta charset="utf-8">
<title>Juniper Anvil — Business Cards and Letterhead</title>
<link rel="stylesheet" href="https://fonts.googleapis.com/css2?family=Source+Sans+3:wght@400;600;700&display=swap">
<style>
:root{
  --bg-top:#34485a;
  --bg-bottom:#8d9ba5;
  --paper:#ffffff;
  --brand-red:#b3151f;
  --ink:#2e2e2e;
  --ink-soft:#4a4a4a;
  --grey-1:#c9c9c9;
  --grey-2:#9a9a9a;
  --grey-3:#6b6b6b;
  --grey-4:#3c3c3c;
  --rule:#8a8a8a;
}
*{margin:0;padding:0;box-sizing:border-box}
html,body{width:1200px;height:900px;overflow:hidden}
body{
  position:relative;
  background:linear-gradient(180deg,var(--bg-top) 0%,var(--bg-bottom) 100%);
  font-family:"Source Sans 3",Arial,sans-serif;
  color:var(--ink);
}
.card{
  position:absolute;left:143px;width:256px;height:152px;
  background:var(--paper);border-radius:10px;overflow:hidden;
}
.wordmark{position:absolute;display:flex;align-items:center;gap:4px;white-space:nowrap}
.wordmark__mark{background:var(--brand-red);flex:none}
.wordmark__name{font-weight:700;color:var(--ink);text-transform:uppercase;letter-spacing:.02em}

/* card front with personal details */
.card--details .wordmark{left:14px;top:12px}
.card--details .wordmark__mark{width:14px;height:14px}
.card--details .wordmark__name{font-size:12px}
.holder{position:absolute;left:150px;width:84px;top:20px;text-align:center}
.holder__name{font-size:10px;font-weight:600;color:var(--ink)}
.holder__role{font-size:6px;color:var(--ink-soft)}
.company{position:absolute;left:15px;top:54px;font-size:6.5px;line-height:9.6px;color:var(--ink)}
.company__name{color:var(--brand-red);font-weight:700}
.company__contact{margin-top:9px}
.company__contact b{color:var(--brand-red)}
.divider{position:absolute;left:134px;top:54px;height:64px;border-left:1px dotted var(--rule)}
.services{position:absolute;left:142px;top:54px;font-size:6px;line-height:9px}
.services__title{color:var(--brand-red);font-weight:700;font-size:6.8px;margin-bottom:1px}
.services li{list-style:none;position:relative;padding-left:6px}
.services li::before{content:"";position:absolute;left:0;top:3.5px;width:2.5px;height:2.5px;background:var(--brand-red)}
.card__rule{position:absolute;left:0;right:0;top:129px;height:2px;background:var(--grey-4)}
.card__band{
  position:absolute;left:0;right:0;top:133px;bottom:0;background:var(--brand-red);
  color:#fff;font-size:7px;text-align:center;line-height:17px;padding-left:20px;
}

/* card back */
.card--brand .wordmark{left:58px;top:48px}
.card--brand .wordmark__mark{width:20px;height:20px}
.card--brand .wordmark__name{font-size:16px}
.strip{position:absolute;left:0;right:0;top:88px;height:16px;display:flex}
.strip span{display:block;height:100%}
.strip__url{flex:1;background:var(--brand-red);color:#fff;font-size:7px;line-height:16px;padding-left:14px}

/* letterhead */
.letterhead{position:absolute;left:472px;top:28px;width:595px;height:840px;background:var(--paper)}
.letterhead .wordmark{left:21px;top:16px}
.letterhead .wordmark__mark{width:26px;height:26px}
.letterhead .wordmark__name{font-size:21px}
.letterhead__topline{position:absolute;left:213px;top:16px;width:382px;height:12px;display:flex}
.letterhead__topline span{display:block;height:100%}
.letter{position:absolute;left:35px;top:147px;width:525px;font-size:13px;line-height:18px;color:var(--ink)}
.letter__salutation{margin-bottom:51px}
.letter p{text-align:justify}
.letter .indent{text-indent:36px}
.letter .gap{margin-top:18px}
.letter__closing{margin-top:18px}
.letter__signer{text-align:right;font-size:11px;margin-top:-1px}
.signature{position:absolute;left:445px;top:612px;width:110px;height:34px;border-radius:4px;
  background:linear-gradient(90deg,#e9e9e9,#f4f4f4)}
.lh-footer{position:absolute;left:44px;top:762px;font-size:8.5px;line-height:11.3px;color:var(--ink)}
.lh-footer__name{color:var(--brand-red);font-weight:600}
.lh-footer--address{padding-left:6px;border-left:1px dotted var(--rule)}
.lh-footer--contact{left:154px;top:766px;padding-left:6px;border-left:1px dotted var(--rule)}
.lh-footer--contact b{color:var(--brand-red);font-weight:600}
.letterhead__base{position:absolute;left:0;right:0;top:818px;height:14px;display:flex}
.letterhead__base span{display:block;height:100%}
.letterhead__reg{flex:1;background:var(--brand-red);color:#fff;font-size:5.5px;line-height:14px;padding-left:6px;white-space:nowrap}
.g1{background:var(--grey-1)}.g2{background:var(--grey-2)}.g3{background:var(--grey-3)}.g4{background:var(--grey-4)}
.red{background:var(--brand-red)}
</style>
</head>
<body>

<section class="card card--details" style="top:74px">
  <div class="wordmark"><span class="wordmark__mark"></span><span class="wordmark__name">Juniper Anvil</span></div>
  <div class="holder"><div class="holder__name">Marcus Telby</div><div class="holder__role">Web Developer</div></div>
  <div class="company">
    <div class="company__name">JUNIPER ANVIL LTD</div>
    <div>Suite 20938, 3rd Floor 212-224</div>
    <div>Orchard Lane London, N7 9QX</div>
    <div class="company__contact"><b>T</b> : 01632 960 418</div>
    <div><b>E</b> : marcus@juniperanvil.example</div>
  </div>
  <div class="divider"></div>
  <ul class="services">
    <li class="services__title" style="padding:0">OUR SERVICES</li>
    <li>Professional Photography</li>
    <li>Web Solutions &amp; E-Commerce</li>
    <li>Audio &amp; HD Video Production</li>
    <li>Marketing &amp; Promotions</li>
    <li>Identity and Branding</li>
  </ul>
  <div class="card__rule"></div>
  <div class="card__band">www.juniperanvil.example</div>
</section>

<section class="card card--brand" style="top:236px">
  <div class="wordmark"><span class="wordmark__mark"></span><span class="wordmark__name">Juniper Anvil</span></div>
  <div class="strip"><span class="g1" style="width:15px"></span><span class="g2" style="width:15px"></span><span class="g3" style="width:15px"></span><span class="g4" style="width:34px"></span><span class="strip__url">www.juniperanvil.example</span></div>
</section>

<section class="card card--details" style="top:472px">
  <div class="wordmark"><span class="wordmark__mark"></span><span class="wordmark__name">Juniper Anvil</span></div>
  <div class="holder"><div class="holder__name">Oliver Brackley</div><div class="holder__role">Photographer</div></div>
  <div class="company">
    <div class="company__name">JUNIPER ANVIL LTD</div>
    <div>Suite 20938, 3rd Floor 212-224</div>
    <div>Orchard Lane London, N7 9QX</div>
    <div class="company__contact"><b>T</b> : 01632 960 418</div>
    <div><b>E</b> : oliver@juniperanvil.example</div>
  </div>
  <div class="divider"></div>
  <ul class="services">
    <li class="services__title" style="padding:0">OUR SERVICES</li>
    <li>Professional Photography</li>
    <li>Web Solutions &amp; E-Commerce</li>
    <li>Audio &amp; HD Video Production</li>
    <li>Marketing &amp; Promotions</li>
    <li>Identity and Branding</li>
  </ul>
  <div class="card__rule"></div>
  <div class="card__band">www.juniperanvil.example</div>
</section>

<section class="card card--brand" style="top:653px">
  <div class="wordmark"><span class="wordmark__mark"></span><span class="wordmark__name">Juniper Anvil</span></div>
  <div class="strip"><span class="g1" style="width:15px"></span><span class="g2" style="width:15px"></span><span class="g3" style="width:15px"></span><span class="g4" style="width:34px"></span><span class="strip__url">www.juniperanvil.example</span></div>
</section>

<section class="letterhead">
  <div class="wordmark"><span class="wordmark__mark"></span><span class="wordmark__name">Juniper Anvil</span></div>
  <div class="letterhead__topline"><span class="red" style="flex:1"></span><span class="g4" style="width:14px"></span><span class="g3" style="width:12px"></span><span class="g2" style="width:12px"></span><span class="g1" style="width:12px"></span></div>

  <div class="letter">
    <div class="letter__salutation">Mr.Marcus Telby</div>
    <p class="indent">Lorem Ipsum is simply dummy text of the printing and typesetting industry. Lorem Ipsum has been the industry's standard dummy text ever since the 1500s, when an unknown printer took a galley of type and scrambled it to make a type specimen book. It has survived not only five centuries, but also the leap into electronic typesetting, remaining essentially unchanged.</p>
    <p>It was popularised in the 1960s with the release of Typeleaf sheets containing Lorem Ipsum passages, and more recently with desktop publishing software like Folio Composer including versions of Lorem Ipsum.</p>
    <p class="gap">There are many variations of passages of Lorem Ipsum available, but the majority have suffered alteration in some form, by injected humour, or randomised words which don't look even slightly believable. If you are going to use a passage of Lorem Ipsum, you need to be sure there isn't anything embarrassing hidden in the middle of text.</p>
    <p class="gap">All the Lorem Ipsum generators on the Internet tend to repeat predefined chunks as necessary, making this the first true generator on the Internet. It uses a dictionary of over 200 Latin words, combined with a handful of model sentence structures, to generate Lorem Ipsum which looks reasonable. The generated Lorem Ipsum is therefore always free from repetition, injected humour, or non-characteristic words etc.</p>
    <div class="letter__closing">Best Regards.</div>
    <div class="letter__signer">Mr. Dorian Vale</div>
  </div>
  <div class="signature" role="img" aria-label="Handwritten signature of the sender"></div>

  <div class="lh-footer lh-footer--address">
    <div class="lh-footer__name">JUNIPER ANVIL LTD</div>
    <div>Suite 20938, 3rd Floor</div>
    <div>212-224 Orchard Lane</div>
    <div>London, N7 9QX</div>
  </div>
  <div class="lh-footer lh-footer--contact">
    <div><b>T</b> : 01632 960 418</div>
    <div><b>E<sub>1</sub></b> : marcus@juniperanvil.example</div>
    <div><b>E<sub>2</sub></b> : oliver@juniperanvil.example</div>
    <div><b>W</b> : www.juniperanvil.example</div>
  </div>

  <div class="letterhead__base"><span class="g1" style="width:14px"></span><span class="g2" style="width:14px"></span><span class="g3" style="width:16px"></span><span class="g4" style="width:106px"></span><span class="letterhead__reg">Juniper Anvil is a Ltd Company registered in England &amp; Wales, Registration No. 05829147.</span></div>
</section>

</body>
</html>
```